Accident Law Firm Billboard Bold Easy to See Car Accidents

We need a billboard design that can catch attention in a very crowed Car Accident lawyer market. We wish to feature the phone number (652) 318-4470 as the focus of the Bill Board. We are trying to get the phone number recognized and remembered by drivers. The law firm name is not as crucial to remember.
Basically, It's CAR ACCIDENT? Then (652) 318-4470. We are not married to any specific color scheme but it has to POP and catch attention.
So the Crucial elements are as follows:
1. Phone number (652) 318-4470
2. Words CAR ACCIDENT?
3. Firm Logo in lower portion or where appropriate. Firm Logo to be provided
4. We may want to try a Day Glow orange color, with White and Black added. An example of the color scheme shall be provided.
5. Possible "Catch Phrase" to be used, "It's Time Call 9"
Target Market(s)
Orlando Florida Car Accident victims
Industry/Entity Type
Law Firm
Requirements
Must have
- Easy to see phone number (652) 318-4470
- Catch attention
Nice to have
- I would like to have the sign visible in bright sunlight and it not too hard to immediately know what phone number is for
Should not have
- too many words
- No bold enough
- confusing fonts
- Unclear fonts

```html
<!DOCTYPE html>
<html lang="en">
<head>
<meta charset="UTF-8">
<title>Car Accident Billboard – Marlowe Law Firm P.C.</title>
<link rel="stylesheet" href="https://fonts.googleapis.com/css2?family=Alfa+Slab+One&family=Special+Elite&display=swap">
<style>
  :root {
    --dayglow-orange: #d8300a;
    --road-black: #000000;
    --crash-tile: #161616;
    --paint-white: #ffffff;
  }
  html, body {
    margin: 0;
    padding: 0;
    overflow: hidden;
    background: var(--dayglow-orange);
  }
  .billboard {
    position: relative;
    width: 1200px;
    height: 350px;
    background: var(--dayglow-orange);
    overflow: hidden;
  }
  .headline {
    position: absolute;
    top: 14px;
    left: 0;
    width: 1200px;
    margin: 0;
    text-align: center;
    font-family: "Special Elite", "Courier New", monospace;
    font-weight: 400;
    font-size: 74px;
    letter-spacing: 3px;
    color: var(--paint-white);
    line-height: 1;
  }
  .road {
    position: absolute;
    top: 110px;
    left: 0;
    width: 1200px;
    height: 112px;
  }
  .call-line {
    position: absolute;
    top: 256px;
    left: 276px;
    margin: 0;
    font-family: "Alfa Slab One", "Rockwell", serif;
    font-size: 33px;
    color: var(--paint-white);
    letter-spacing: 0.5px;
    line-height: 1;
    white-space: nowrap;
  }
  .call-line .phone {
    margin-left: 10px;
  }
  .firm-name {
    position: absolute;
    top: 286px;
    left: 986px;
    margin: 0;
    font-family: "Alfa Slab One", "Rockwell", serif;
    color: var(--paint-white);
    line-height: 1;
  }
  .firm-name .firm-primary {
    display: block;
    font-size: 23px;
    letter-spacing: 0.5px;
  }
  .firm-name .firm-secondary {
    display: block;
    margin-top: 3px;
    font-size: 13px;
    letter-spacing: 1.6px;
  }
</style>
</head>
<body>
  <main class="billboard">
    <h1 class="headline">CAR ACCIDENT?</h1>

    <svg class="road" viewBox="0 0 1200 112" width="1200" height="112" aria-hidden="true">
      <rect class="road-edge" x="0" y="0" width="1200" height="4" fill="var(--paint-white)"/>
      <rect class="road-surface" x="0" y="4" width="1200" height="104" fill="var(--road-black)"/>
      <rect class="road-edge" x="0" y="108" width="1200" height="4" fill="var(--paint-white)"/>
      <g class="lane-dashes" fill="var(--paint-white)">
        <rect x="0" y="53" width="24" height="3"/>
        <rect x="92" y="53" width="28" height="3"/>
        <rect x="172" y="53" width="28" height="3"/>
        <rect x="248" y="53" width="28" height="3"/>
        <rect x="324" y="53" width="28" height="3"/>
        <rect x="400" y="53" width="28" height="3"/>
        <rect x="464" y="53" width="24" height="3"/>
        <rect x="648" y="53" width="28" height="3"/>
        <rect x="728" y="53" width="28" height="3"/>
        <rect x="808" y="53" width="28" height="3"/>
        <rect x="876" y="53" width="28" height="3"/>
        <rect x="946" y="53" width="28" height="3"/>
        <rect x="1020" y="53" width="28" height="3"/>
        <rect x="1096" y="53" width="28" height="3"/>
        <rect x="1176" y="53" width="24" height="3"/>
      </g>
      <rect class="crash-icon" x="508" y="4" width="116" height="104" fill="var(--crash-tile)" role="img" aria-label="Icon of two white cars colliding on the road"/>
    </svg>

    <p class="call-line">IT'S TIME CALL <span class="phone">(652) 318-4470</span></p>

    <p class="firm-name">
      <span class="firm-primary">MARLOWE</span>
      <span class="firm-secondary">LAW FIRM P.C.</span>
    </p>
  </main>
</body>
</html>
```